Business Card Design

Velvet Pixel Promotions

An online marketing consulting & strategy business for the cosmetic niche

We specialise in Increasing Leads, Conversions & Content Marketing

I am looking for a very clean, BOLD business card that is simple & effective

Target Market(s)

cosmetic surgeons & cosmetic clinics

Industry/Entity Type

Marketing

Contact Information for Business Card

Darren Okoye
Online Marketing Strategist

Darren@VelvetPixelPromotions.example
0491 268 517

LinkedIn: in/darrenokoye

```html
<!DOCTYPE html>
<html lang="en">
<head>
<meta charset="utf-8">
<title>Velvet Pixel Promotions – Business Card</title>
<link rel="stylesheet" href="https://fonts.googleapis.com/css2?family=Saira:wght@500&family=Arimo:wght@400;500&display=swap">
<style>
  :root {
    --stage: #a9a9a9;
    --blue: #35a9df;
    --green: #a2cd3b;
    --white: #ffffff;
    --ink: #5b6067;
    --text: #4a4f55;
    --faint-green: #eef4dc;
  }
  * { box-sizing: border-box; margin: 0; padding: 0; }
  html, body { width: 1200px; height: 900px; overflow: hidden; }
  body { background: var(--stage); position: relative; font-family: "Saira", "Arial", sans-serif; }

  .card {
    position: absolute;
    width: 566px;
    overflow: hidden;
    box-shadow: 3px 4px 5px rgba(0,0,0,0.45);
  }
  .card--square { height: 340px; }
  .card--rounded { height: 326px; border-radius: 22px; }

  .row-top .card { top: 110px; }
  .row-bottom .card { top: 486px; }
  .card-front { left: 18px; background: linear-gradient(180deg, var(--blue) 0%, #6cb8ad 45%, var(--green) 100%); }
  .card-back { left: 613px; background: var(--white); }

  /* front wordmark */
  .wordmark {
    position: absolute;
    left: 106px; top: 50%;
    transform: translateY(-50%);
    display: flex; align-items: center; gap: 16px;
    color: var(--white);
  }
  .wordmark-mark {
    width: 82px; height: 82px;
    border: 10px solid var(--white);
    border-radius: 50%;
  }
  .wordmark-name { font-weight: 500; font-size: 37px; line-height: 31px; letter-spacing: 2px; text-transform: uppercase; }
  .wordmark-name span { display: block; }
  .wordmark-name .wide { letter-spacing: 9.5px; }

  /* back frame */
  .frame-top, .frame-bottom { position: absolute; left: 0; right: 0; }
  .frame-top { top: 3px; height: 9px; border-top: 4px solid var(--blue); border-bottom: 3px solid var(--green); }
  .frame-bottom { bottom: 6px; height: 8px; border-top: 3px solid var(--green); border-bottom: 3px solid var(--blue); }
  .frame-side { position: absolute; top: 3px; bottom: 6px; width: 6px; background: linear-gradient(180deg, var(--blue), var(--green)); }
  .frame-side--left { left: 5px; }
  .frame-side--right { right: 10px; }

  .backdrop-ring {
    position: absolute;
    left: 228px; top: 20px;
    width: 330px; height: 330px;
    border-radius: 50%;
    border: 42px solid var(--faint-green);
  }

  .back-name {
    position: absolute; left: 34px; top: 30px;
    display: flex; align-items: center; gap: 10px;
    color: var(--ink);
  }
  .back-name-mark { width: 58px; height: 58px; border: 7px solid var(--blue); border-radius: 50%; }
  .back-name-text { font-weight: 500; font-size: 25px; line-height: 21px; letter-spacing: 1.5px; text-transform: uppercase; }
  .back-name-text span { display: block; }
  .back-name-text .wide { letter-spacing: 6.5px; }

  .contact-list { position: absolute; left: 281px; list-style: none; font-family: "Arimo", "Arial", sans-serif; font-weight: 500; font-size: 13px; color: var(--text); }
  .row-top .contact-list { top: 235px; }
  .row-bottom .contact-list { top: 224px; }
  .contact-list li { display: flex; align-items: center; gap: 9px; height: 32px; }
  .row-bottom .contact-list li { height: 31px; }
  .contact-icon { width: 19px; height: 19px; background: var(--blue); display: flex; align-items: center; justify-content: center; flex: none; }
  .contact-icon svg { width: 15px; height: 15px; }
</style>
</head>
<body>

<section class="row-top">
  <div class="card card--square card-front">
    <div class="wordmark">
      <div class="wordmark-mark"></div>
      <div class="wordmark-name"><span>Velvet</span><span class="wide">Pixel</span><span>Promotions</span></div>
    </div>
  </div>
  <div class="card card--square card-back">
    <div class="backdrop-ring"></div>
    <div class="frame-top"></div>
    <div class="frame-side frame-side--left"></div>
    <div class="frame-side frame-side--right"></div>
    <div class="frame-bottom"></div>
    <div class="back-name">
      <div class="back-name-mark"></div>
      <div class="back-name-text"><span>Velvet</span><span class="wide">Pixel</span><span>Promotions</span></div>
    </div>
    <ul class="contact-list">
      <li><span class="contact-icon"><svg viewBox="0 0 16 16" fill="none" stroke="#fff" stroke-width="1.2"><circle cx="8" cy="8" r="6.5"/><ellipse cx="8" cy="8" rx="3" ry="6.5"/><line x1="1.5" y1="8" x2="14.5" y2="8"/></svg></span>0491 268 517</li>
      <li><span class="contact-icon"><svg viewBox="0 0 16 16" fill="none" stroke="#fff" stroke-width="1.2"><rect x="1.5" y="3.5" width="13" height="9"/><polyline points="1.5,3.5 8,9 14.5,3.5"/></svg></span>Darren@VelvetPixelPromotions.example</li>
      <li><span class="contact-icon"><svg viewBox="0 0 16 16" fill="none" stroke="#fff" stroke-width="1.4" stroke-linecap="round"><path d="M7 9.5 L9.5 7"/><path d="M6.2 7.3 L4.3 9.2 a2 2 0 0 0 2.8 2.8 L9 10.1"/><path d="M9.8 8.7 L11.7 6.8 a2 2 0 0 0 -2.8 -2.8 L7 5.9"/></svg></span>in/darrenokoye</li>
    </ul>
  </div>
</section>

<section class="row-bottom">
  <div class="card card--rounded card-front">
    <div class="wordmark">
      <div class="wordmark-mark"></div>
      <div class="wordmark-name"><span>Velvet</span><span class="wide">Pixel</span><span>Promotions</span></div>
    </div>
  </div>
  <div class="card card--rounded card-back">
    <div class="backdrop-ring"></div>
    <div class="frame-top"></div>
    <div class="frame-side frame-side--left"></div>
    <div class="frame-side frame-side--right"></div>
    <div class="frame-bottom"></div>
    <div class="back-name">
      <div class="back-name-mark"></div>
      <div class="back-name-text"><span>Velvet</span><span class="wide">Pixel</span><span>Promotions</span></div>
    </div>
    <ul class="contact-list">
      <li><span class="contact-icon"><svg viewBox="0 0 16 16" fill="none" stroke="#fff" stroke-width="1.2"><circle cx="8" cy="8" r="6.5"/><ellipse cx="8" cy="8" rx="3" ry="6.5"/><line x1="1.5" y1="8" x2="14.5" y2="8"/></svg></span>0491 268 517</li>
      <li><span class="contact-icon"><svg viewBox="0 0 16 16" fill="none" stroke="#fff" stroke-width="1.2"><rect x="1.5" y="3.5" width="13" height="9"/><polyline points="1.5,3.5 8,9 14.5,3.5"/></svg></span>Darren@VelvetPixelPromotions.example</li>
      <li><span class="contact-icon"><svg viewBox="0 0 16 16" fill="none" stroke="#fff" stroke-width="1.4" stroke-linecap="round"><path d="M7 9.5 L9.5 7"/><path d="M6.2 7.3 L4.3 9.2 a2 2 0 0 0 2.8 2.8 L9 10.1"/><path d="M9.8 8.7 L11.7 6.8 a2 2 0 0 0 -2.8 -2.8 L7 5.9"/></svg></span>in/darrenokoye</li>
    </ul>
  </div>
</section>

</body>
</html>
```